Psychotherapist's business card

I need a business card design for a psychotherapist. I expect business card to have "light" design. By this I mean that it can somehow translate easiness, serenity. Maybe pastel colours can help you here. I have attached some pictures from Greece. Perhaps they can inspire you to combine colours and to achieve that "light" design.
Updates

Pls, don't use any free samples you may find on business card generators. It looks too simple, uncreative and waste of time! READ size and colour requirements! I don't want to see any shapes like rings, triangles etc.

Contact Information for Business Card

Size: 65mmX60mm

Name - Мирослав Гречихин

Психолог
+7(916)482-39-07
grechikhin.com

I suppose that thin font can look good but it's up to you

Requirements
Must have
• size requirements
Nice to have
• pastel colours
• thin font
Should not have
• black and dark colours
• lines, free design samples used from other web-sites

```html
<!DOCTYPE html>
<html lang="ru">
<head>
<meta charset="utf-8">
<title>Мирослав Гречихин — визитка психолога</title>
<link rel="stylesheet" href="https://fonts.googleapis.com/css2?family=Exo+2:wght@200;300;400&display=swap">
<style>
  :root {
    --backdrop: #d9d9d9;
    --teal: #43a8a2;
    --gold: #c99a34;
    --paper: #f6f6f4;
    --ink: #5a5a5a;
    --ink-soft: #6b6b6b;
    --white: #ffffff;
  }
  * { margin: 0; padding: 0; box-sizing: border-box; }
  html, body {
    width: 1200px;
    height: 764px;
    overflow: hidden;
    background: var(--backdrop);
    font-family: "Exo 2", "Helvetica Neue", Arial, sans-serif;
  }
  .canvas {
    position: relative;
    width: 1200px;
    height: 764px;
  }
  /* 65 × 60 mm proportion */
  .card {
    position: absolute;
    top: 182px;
    width: 433px;
    height: 400px;
    overflow: hidden;
  }
  .card--front {
    left: 117px;
    background: var(--teal);
  }
  .card--back {
    left: 650px;
    background: var(--paper);
  }
  .gold-field {
    position: absolute;
    top: 0;
    right: 0;
    width: 64px;
    height: 100%;
    background: var(--gold);
    opacity: 0.85;
  }
  .front-name {
    position: absolute;
    left: 40px;
    bottom: 48px;
    color: var(--white);
    font-weight: 300;
    font-size: 34px;
    line-height: 1.1;
    letter-spacing: 0.5px;
    text-transform: lowercase;
  }
  .back-content {
    position: absolute;
    inset: 0;
    display: flex;
    flex-direction: column;
    align-items: center;
    justify-content: center;
    text-align: center;
    padding: 0 24px;
  }
  .back-name {
    color: var(--ink);
    font-weight: 400;
    font-size: 21px;
    letter-spacing: 1.5px;
    text-transform: uppercase;
    word-spacing: 6px;
  }
  .profession {
    margin-top: 8px;
    margin-bottom: 34px;
    color: var(--teal);
    font-weight: 300;
    font-size: 16px;
    letter-spacing: 0.5px;
  }
  .contacts {
    list-style: none;
    color: var(--ink-soft);
    font-weight: 300;
    font-size: 14px;
    line-height: 1.45;
    letter-spacing: 0.6px;
    text-transform: uppercase;
  }
</style>
</head>
<body>
  <main class="canvas">
    <section class="card card--front" aria-label="Лицевая сторона визитки">
      <span class="gold-field"></span>
      <h1 class="front-name">Мирослав<br>Гречихин</h1>
    </section>

    <section class="card card--back" aria-label="Оборотная сторона визитки">
      <div class="back-content">
        <h2 class="back-name">Мирослав Гречихин</h2>
        <p class="profession">психолог</p>
        <ul class="contacts">
          <li>+7(916)482-39-07</li>
          <li>psygrech@grechikhin.com</li>
          <li>grechikhin.com</li>
        </ul>
      </div>
    </section>
  </main>
</body>
</html>
```